CCTV Website

We are looking for a Wordpress designer to create an e-commerce website for us. We have all the products that will be uploaded to site on csv format, so our main focus is layout, style, home page slider image selections and related site page images selection by the designer.

When project is reaching completion we will provide product files.

Industry/Entity Type

E-Commerce

```html
<!DOCTYPE html>
<html lang="en">
<head>
<meta charset="utf-8">
<title>Kestrel Securities</title>
<link href="https://fonts.googleapis.com/css2?family=Roboto+Slab:wght@300;400&family=Roboto:wght@400;500&display=swap" rel="stylesheet">
<style>
:root{
  --green:#8dc63f;
  --green-soft:#9fd05a;
  --ink:#333333;
  --text:#7a7a7a;
  --line:#ececec;
  --footer:#f2f2f2;
  --bar:#4a4a4a;
  --white:#ffffff;
}
*{box-sizing:border-box;margin:0;padding:0}
html,body{width:1200px;height:2335px;overflow:hidden;background:var(--white)}
body{position:relative;font-family:"Roboto",Arial,sans-serif;color:var(--text)}
h1,h2,h3{font-weight:400}
.abs{position:absolute}

/* header */
.site-header{position:absolute;left:0;top:0;width:1200px;height:101px;background:var(--white);border-top:3px solid var(--green)}
.brand{position:absolute;left:86px;top:22px;display:flex;align-items:center;gap:18px}
.brand-dot{width:56px;height:56px;border-radius:50%;background:var(--green)}
.brand-name{font-family:"Roboto Slab",Georgia,serif;font-size:30px;font-weight:400;color:#444}
.main-nav a{position:absolute;top:46px;font-size:12px;color:var(--ink);text-decoration:none;text-transform:uppercase;letter-spacing:.2px}
.main-nav a.active{color:var(--green)}

/* hero */
.hero{position:absolute;left:0;top:101px;width:1200px;height:560px;background:
  radial-gradient(ellipse 190px 220px at 330px 250px,rgba(236,236,232,.95),rgba(236,236,232,0) 70%),
  radial-gradient(ellipse 170px 260px at 600px 340px,rgba(120,150,90,.55),rgba(120,150,90,0) 70%),
  radial-gradient(ellipse 260px 300px at 1080px 300px,rgba(210,215,220,.7),rgba(210,215,220,0) 70%),
  linear-gradient(100deg,#1f2c38 0%,#4d5f6e 22%,#8f9ca6 45%,#7e8a93 62%,#5a6873 82%,#3b4954 100%)}
.hero-title{position:absolute;left:669px;top:106px;font-family:"Roboto Slab",Georgia,serif;font-weight:300;font-size:58px;line-height:64px}
.hero-title .a{color:var(--green);display:block}
.hero-title .b{color:var(--white);display:block;text-shadow:0 2px 4px rgba(0,0,0,.35)}
.hero-copy{position:absolute;left:671px;top:264px;width:380px;font-size:12.5px;line-height:26px;color:#f0f0f0}
.pill{position:absolute;background:var(--green);color:var(--white);font-family:"Roboto Slab",Georgia,serif;font-weight:400;font-size:17px;border-radius:26px;display:flex;align-items:center;justify-content:center}

/* services card */
.services{position:absolute;left:86px;top:607px;width:1027px;height:482px;background:var(--white)}
.photo{position:absolute}
.photo-res{left:15px;top:18px;width:482px;height:240px;background:
  radial-gradient(ellipse 150px 70px at 340px 150px,rgba(90,90,90,.8),rgba(90,90,90,0) 75%),
  linear-gradient(90deg,#d9d9d9 0%,#f2f2f2 25%,#c8c8c8 45%,#e9e9e9 70%,#8a8a8a 100%)}
.photo-corp{left:532px;top:18px;width:482px;height:240px;background:
  radial-gradient(ellipse 90px 120px at 110px 120px,rgba(245,245,245,.95),rgba(245,245,245,0) 75%),
  linear-gradient(90deg,#e4e6e8 0%,#f4f4f4 30%,#9aa3aa 55%,#4c5660 75%,#22282e 100%)}
.service-title{position:absolute;font-family:"Roboto Slab",Georgia,serif;font-weight:400;font-size:23px;color:var(--green)}
.service-copy{position:absolute;width:470px;font-size:11.5px;line-height:26px;color:var(--text)}
.tab-btn{position:absolute;height:42px;display:flex;align-items:center}
.tab-btn span{display:flex;align-items:center;height:42px;padding:0 18px 0 12px;background:var(--green);color:var(--white);font-family:"Roboto Slab",Georgia,serif;font-size:16px}

/* welcome */
.welcome-title{position:absolute;left:86px;top:1138px;font-family:"Roboto Slab",Georgia,serif;font-weight:400;font-size:25px;color:var(--green)}
.welcome-copy{position:absolute;left:86px;width:490px;font-size:11.5px;line-height:25.5px}
.devices{position:absolute;left:666px;top:1164px;width:448px;height:305px;background:
  radial-gradient(ellipse 70px 110px at 390px 190px,rgba(20,20,20,.95),rgba(20,20,20,0) 80%),
  radial-gradient(ellipse 70px 40px at 120px 70px,rgba(60,60,60,.7),rgba(60,60,60,0) 80%),
  linear-gradient(180deg,#e9eaeb 0%,#f6f6f6 55%,#d6d8da 78%,#bfc2c5 100%)}

/* testimonial */
.testimonial{position:absolute;left:0;top:1536px;width:1200px;height:261px;background:var(--green)}
.avatar{position:absolute;left:235px;top:65px;width:134px;height:134px;border-radius:50%;border:4px solid var(--white);background:radial-gradient(circle at 50% 40%,#e3d6c8,#b8a796 60%,#7c6c5e)}
.quote{position:absolute;left:414px;top:72px;width:540px;font-size:12px;line-height:25px;color:var(--white)}
.qmark{position:absolute;font-family:Georgia,serif;font-size:30px;color:#eaf5dc}
.author{position:absolute;left:414px;top:160px;font-family:"Roboto Slab",Georgia,serif;font-size:13px;color:var(--white);line-height:22px}

/* partners */
.partners{position:absolute;left:0;top:1797px;width:1200px;height:218px;background:var(--white)}
.badge{position:absolute;top:55px;width:181px;height:105px;border:5px solid #efefef;background:var(--white)}
.badge i{position:absolute;left:50%;top:50%;width:40px;height:40px;margin:-20px 0 0 -20px;border-radius:50%;background:#d3d3d3}

/* footer */
.site-footer{position:absolute;left:0;top:2015px;width:1200px;height:257px;background:var(--footer)}
.foot-h{position:absolute;top:48px;font-size:15px;font-weight:500;color:var(--ink);letter-spacing:.3px}
.links{position:absolute;left:117px;top:88px;list-style:none}
.links li{height:25px;font-size:12px;color:#555;display:flex;align-items:center}
.links li b{width:38px;color:#666;font-weight:400;font-size:12px}
.contact{position:absolute;left:328px;top:88px}
.contact div{display:flex;align-items:flex-start;font-size:12px;color:#555;height:29px}
.contact svg{width:14px;height:14px;margin-right:12px;margin-top:1px;flex:none}
.foot-copy{position:absolute;font-size:12px;line-height:20px;color:#666}
.email-field{position:absolute;left:616px;top:2150px;width:212px;height:32px;border:1px solid #d4d4d4;background:var(--white);font-size:12px;color:#666;padding:8px 12px}
.subscribe{position:absolute;left:616px;top:2192px;width:81px;height:27px;background:var(--green);color:var(--white);font-size:11px;display:flex;align-items:center;justify-content:center}
.social{position:absolute;left:892px;top:2161px;display:flex;gap:8px}
.social span{width:35px;height:35px;border-radius:50%;border:2px solid #bdbdbd;display:flex;align-items:center;justify-content:center}
.social span::after{content:"";width:11px;height:11px;border-radius:50%;background:#bdbdbd}
.bottom-bar{position:absolute;left:0;top:2272px;width:1200px;height:63px;background:var(--bar);color:#eee;font-size:12px;display:flex;align-items:center;justify-content:center}
</style>
</head>
<body>

<header class="site-header">
  <div class="brand"><span class="brand-dot"></span><span class="brand-name">Kestrel Securities</span></div>
  <nav class="main-nav">
    <a class="active" href="#" style="left:591px">Home</a>
    <a href="#" style="left:666px">About Us</a>
    <a href="#" style="left:766px">Services</a>
    <a href="#" style="left:864px">Projects</a>
    <a href="#" style="left:962px">News</a>
    <a href="#" style="left:1038px">Contact Us</a>
  </nav>
</header>

<section class="hero" role="img" aria-label="Dome security camera mounted in a bright office building">
  <h1 class="hero-title"><span class="a">Kestrel</span><span class="b">Securities</span></h1>
  <p class="hero-copy">Sed ut perspiciatis unde omnis iste natus error sit voluptatem accusantium doloremque laudantium, totam rem aperiam, eaque ipsa quae ab illo inventore veritatis explicabo.</p>
  <div class="pill" style="left:672px;top:363px;width:165px;height:47px">Read More</div>
</section>

<section class="services">
  <div class="photo photo-res" role="img" aria-label="Security camera on an apartment building facade"></div>
  <div class="photo photo-corp" role="img" aria-label="Operator watching CCTV monitors in a control room"></div>

  <h2 class="service-title" style="left:17px;top:276px">Residential</h2>
  <p class="service-copy" style="left:18px;top:319px">Sed ut perspiciatis unde omnis iste natus error sit voluptatem accusantium doloremque laudantium, totam rem aperiam, eaque ipsa quae ab illo inventore veritatis et quasi archi ipsam voluptatem quia tecto beatae vitae dicta sunt explicabo.</p>
  <div class="tab-btn" style="left:18px;top:412px"><span>Read More</span>
    <svg width="34" height="42" viewBox="0 0 34 42"><path d="M0 0h8l14 42h-8z" fill="#555"/><path d="M12 0h6l14 42h-6z" fill="#555"/></svg></div>

  <h2 class="service-title" style="left:534px;top:276px">Corporate Customers</h2>
  <p class="service-copy" style="left:535px;top:319px">Sed ut perspiciatis unde omnis iste natus error sit voluptatem accusantium doloremque laudantium, totam rem aperiam, eaque ipsa quae ab illo inventore veritatis et quasi archi ipsam voluptatem quia tecto beatae vitae dicta sunt explicabo.</p>
  <div class="tab-btn" style="left:535px;top:412px"><span>Read More</span>
    <svg width="34" height="42" viewBox="0 0 34 42"><path d="M0 0h8l14 42h-8z" fill="#555"/><path d="M12 0h6l14 42h-6z" fill="#555"/></svg></div>
</section>

<h2 class="welcome-title">Welcome To Kestrel Securities</h2>
<p class="welcome-copy" style="top:1193px">Sed ut perspiciatis unde omnis iste natus error sit voluptatem accusantium doloremque laudantium, totam rem aperiam, eaque ipsa quae ab illo inventore veritatis et quasi archi tecto beatae vitae dicta sunt explicabo. Nemo enim ipsam voluptatem quia voluptas sit asp ern atur aut odit aut fugit, sed quia consequuntur magni</p>
<p class="welcome-copy" style="top:1325px">Sed ut perspiciatis unde omnis iste natus error sit voluptatem accusantium doloremque laudantium, totam rem aperiam, eaque ipsa quae ab illo inventore veritatis et quasi archi tecto voluptatem quia voluptas sit asp ern atur aut odit aut fugit</p>
<div class="pill" style="left:87px;top:1434px;width:171px;height:50px;font-size:16px">Read More Info</div>
<div class="devices" role="img" aria-label="Desktop monitor and tablet showing security cameras and an alarm keypad"></div>

<section class="testimonial">
  <div class="avatar" role="img" aria-label="Portrait of the customer"></div>
  <span class="qmark" style="left:388px;top:58px">“</span>
  <p class="quote">Sed ut perspiciatis unde omnis iste natus error sit voluptatem accusantium doloremque laudantium, totam rem aperiam, eaque ipsa quae ab illo inventore veritatis et quasi architecto beatae vitae dicta sunt explicabo. Nemo enim ipsam voluptatem quia voluptas sit aspernatur</p>
  <span class="qmark" style="left:818px;top:120px">”</span>
  <div class="author">DANA PORTER<br>Posed on 25 Feb 2018</div>
</section>

<section class="partners">
  <svg class="abs" style="left:46px;top:85px" width="20" height="64" viewBox="0 0 20 64"><path d="M18 2L3 32l15 30" fill="none" stroke="#cfcfcf" stroke-width="2"/></svg>
  <div class="badge" style="left:103px"><i></i></div>
  <div class="badge" style="left:305px"><i></i></div>
  <div class="badge" style="left:512px"><i></i></div>
  <div class="badge" style="left:716px"><i></i></div>
  <div class="badge" style="left:920px"><i></i></div>
  <svg class="abs" style="left:1138px;top:85px" width="20" height="64" viewBox="0 0 20 64"><path d="M2 2l15 30L2 62" fill="none" stroke="#cfcfcf" stroke-width="2"/></svg>
</section>

<footer class="site-footer">
  <h3 class="foot-h" style="left:117px">QUICK LINKS</h3>
  <ul class="links">
    <li><b>»</b>Home</li><li><b>»</b>About Us</li><li><b>»</b>Services</li><li><b>»</b>Projects</li><li><b>»</b>News</li><li><b>»</b>Contact Us</li>
  </ul>

  <h3 class="foot-h" style="left:328px">CONTACT US</h3>
  <div class="contact">
    <div><svg viewBox="0 0 14 14"><path d="M1 4c0-2 2-3 6-3s6 1 6 3v1H9V4H5v1H1z M3 6h8l2 6H1z" fill="#777"/></svg>(000)-555-0142 (Phone)</div>
    <div><svg viewBox="0 0 14 14"><rect x="3" y="1" width="8" height="4" fill="#777"/><rect x="1" y="5" width="12" height="6" rx="1" fill="#777"/><rect x="3" y="9" width="8" height="4" fill="#aaa"/></svg>(000)-555-0143 (Fax)</div>
    <div><svg viewBox="0 0 14 14"><rect x="1" y="3" width="12" height="9" fill="#777"/><path d="M1 3l6 5 6-5" fill="none" stroke="#eee" stroke-width="1.2"/></svg><span style="text-decoration:underline">info@kestrelsecurities.com</span></div>
    <div style="height:40px"><svg viewBox="0 0 14 14"><path d="M7 1a4 4 0 0 1 4 4c0 3-4 8-4 8S3 8 3 5a4 4 0 0 1 4-4z" fill="#777"/><circle cx="7" cy="5" r="1.5" fill="#f2f2f2"/></svg><span style="line-height:16px">70 Lorem Ipsum Dummy Text<br>Lorem Ipsum</span></div>
  </div>

  <h3 class="foot-h" style="left:615px">NEWSLETTER</h3>
  <p class="foot-copy" style="left:616px;top:86px;width:210px">Register Your email address to get information ablout us</p>

  <h3 class="foot-h" style="left:893px;top:50px">FOLLOW US</h3>
  <p class="foot-copy" style="left:893px;top:86px;width:195px">Lorem ipsum dolor sit amet, conse ctetur adipiscing elit. Nulla in purus nibh. Donec ornare</p>
</footer>
<div class="email-field">Email Address</div>
<div class="subscribe">SUBSCRIBE</div>
<div class="social"><span></span><span></span><span></span><span></span><span></span></div>

<div class="bottom-bar">© Copyright 2018 Kestrel Securities.All Rights Reserved</div>

</body>
</html>
```